Brantley Estates is a commercial real estate development company based in the United States. We develop high-end office buildings and student housing apartments. We have a new logo and need to update all of our stationary items and business cards. We would like the design to be clean and professional. Our logo and color information is attached. Our logo MUST be in full color and not as white. It is preferred that the logo is on a white background.

Color code Blue R 0. G 62. B 124 ( #003E7C )
C 100 M84 Y 26 K 22
Black R32. G30. B30 ( #201E1E)
C100 M100 Y100 K100

Font used TRAJAN PRO3 PRO BOLD.

Items needed:
1. Business card - Leaning towards doing just a one side business card in a thicker paper. Include - logo, name - Martin E. Caldwell, Title - Chairman & CEO, 5120 Ridgemont Pkwy. Suite 400, Atlanta, GA 30327 - Cell number 404.617.####, Office 770.245.62## email@brantleyestates.com; www.brantleyestates.com.

2. Letterhead - Standard 8.5 by 11 paper. We do have a smaller size for the CEO that is 7.25 by 10.5 that is just a mirror of the letterhead except with his name (Martin E. Caldwell) and title (Chariman & CEO) listed at the top in the header. Letthead needs address, phone number and website, plus logo. *Prepared such that we can either implement as a Google Document template or professionally print.

3. Legal sized envelope - #10 envelope - which measures 4 1/8" by 9 1/2". We also use the same size envelope with a window. Need logo and address. A photo of the old envelope style is attached.

4. 9" x 12" Pocket folder - Need a design that can also be split to be a cover page and back - We use the cover pages in spiral binding machine, so we need to leave room on the left for that. One of the pockets should hold a business card. Include logo, address, phone, website. Also if text is needed, we could say development / leasing / property management.

5. Shipping label - 3 1/3" x 4" inches and 6 per page. Just need logo and address listed at top of the label and white space at bottom.

Company: Brantley Estates
Address: 5120 Ridgemont Pkwy. Suite 400, Atlanta, GA 30327
Phone: 770.245.6274
Fax: 770.245.6219 (probably not needed)
Website: www.brantleyestates.com

Thank you for all your help!

Target Market(s)

Should communicate a strong corporate feel

Contact Information for Business Card

Include - logo, name - Martin E. Caldwell, Title - Chairman & CEO, 5120 Ridgemont Pkwy. Suite 400, Atlanta, GA 30327 - Cell number 404.617.####, Office 770.245.62## email@brantleyestates.com; www.brantleyestates.com.

Logo Text

Brantley Estates

Colors

Designer to choose colors to be used in the design.

Requirements
Must have
• Our logo MUST be in full color and not as white. It is preferred that the logo is on a white background.
• Colors - Color code Blue R 0. G 62. B 124 ( #003E7C )
• C 100 M84 Y 26 K 22
Nice to have
• Font used in logo TRAJAN PRO3 PRO BOLD. Would love to see options of both a one sided and double-sided.
Should not have
• Logo in white.

```html
<!DOCTYPE html>
<html lang="en">
<head>
<meta charset="utf-8">
<title>Brantley Estates – Pocket Folder</title>
<link href="https://fonts.googleapis.com/css2?family=Cinzel:wght@400;700&display=swap" rel="stylesheet">
<style>
  :root {
    --navy: #26386a;
    --navy-deep: #1f2f5c;
    --paper: #ffffff;
    --paper-grey: #e4e4e4;
    --stage: #a9b7d2;
    --ink-light: #ffffff;
  }
  * { box-sizing: border-box; margin: 0; padding: 0; }
  html, body { width: 1200px; height: 847px; overflow: hidden; }
  body {
    background: var(--stage);
    font-family: "Cinzel", "Times New Roman", serif;
    position: relative;
  }
  .panel {
    position: absolute;
    top: 183px;
    width: 360px;
    height: 480px;
    overflow: hidden;
  }
  .front-cover {
    left: 40px;
    background: linear-gradient(135deg, #f4f4f4 0%, #dcdcdc 100%);
    box-shadow: 0 10px 24px rgba(30, 45, 80, .25);
  }
  .cover-strip {
    position: absolute; left: 0; right: 0; bottom: 0; height: 5px;
    background: var(--navy);
  }
  .wordmark {
    position: absolute; left: 48px; top: 86px;
    display: flex; align-items: center; gap: 10px;
    color: var(--navy); font-weight: 700;
  }
  .wordmark-dot {
    width: 40px; height: 40px; border-radius: 50%;
    background: var(--navy); flex: none;
  }
  .wordmark-name { font-size: 26px; line-height: 1.05; letter-spacing: 1px; }
  .wordmark-name span { display: block; }
  .wordmark-name .sub { font-size: 15px; letter-spacing: 5px; }

  .spread { left: 440px; width: 720px; box-shadow: 0 10px 24px rgba(30, 45, 80, .25); }
  .inside-left { left: 0; top: 0; width: 360px; background: linear-gradient(120deg, #fafafa 0%, #ededed 60%, #f7f7f7 100%); }
  .inside-right { left: 360px; top: 0; width: 360px; background: #dedede; border-left: 1px solid #c9c9c9; }
  .spread .panel { position: absolute; top: 0; }

  .pocket {
    position: absolute; left: 0; right: 0; bottom: 0; height: 150px;
    background: var(--navy); color: var(--ink-light);
  }
  .contact-list { list-style: none; padding: 18px 0 0 24px; }
  .contact-list li {
    display: flex; align-items: flex-start; gap: 7px;
    font-size: 13.5px; line-height: 1.25; margin-bottom: 8px;
  }
  .contact-list svg { width: 13px; height: 13px; flex: none; margin-top: 2px; }
  .contact-list .inline-icon { display: inline-block; vertical-align: -2px; margin: 0 3px 0 6px; }

  .card-slot {
    position: absolute; left: 182px; top: 14px; width: 156px; height: 90px;
  }
  .business-card {
    position: absolute; inset: 0;
    background: var(--paper); color: var(--navy);
    box-shadow: 2px 3px 5px rgba(0,0,0,.35);
    display: flex; align-items: center; padding: 8px;
    clip-path: polygon(8px 0, calc(100% - 8px) 0, 100% 8px, 100% calc(100% - 8px), calc(100% - 8px) 100%, 8px 100%, 0 calc(100% - 8px), 0 8px);
  }
  .card-brand { display: flex; align-items: center; gap: 3px; font-weight: 700; font-size: 6.5px; line-height: 1.05; width: 64px; }
  .card-brand .dot { width: 9px; height: 9px; border-radius: 50%; background: var(--navy); flex: none; }
  .card-details { border-left: 1px solid #c7cbd6; padding-left: 5px; font-size: 3.6px; line-height: 1.45; color: #444; }
  .card-details .name { font-size: 5.2px; font-weight: 700; color: var(--navy); }
  .services {
    position: absolute; left: 14px; right: 10px; bottom: 18px;
    font-size: 11px; font-weight: 700; letter-spacing: .3px; white-space: nowrap;
  }
</style>
</head>
<body>

<section class="panel front-cover" aria-label="Folder front cover">
  <div class="wordmark">
    <div class="wordmark-dot"></div>
    <div class="wordmark-name"><span>BRANTLEY</span><span class="sub">ESTATES</span></div>
  </div>
  <div class="cover-strip"></div>
</section>

<section class="panel spread" aria-label="Folder inside spread">
  <div class="panel inside-left">
    <div class="pocket">
      <ul class="contact-list">
        <li>
          <svg viewBox="0 0 16 16"><path d="M8 1a5 5 0 0 0-5 5c0 4 5 9 5 9s5-5 5-9a5 5 0 0 0-5-5zm0 7a2 2 0 1 1 0-4 2 2 0 0 1 0 4z" fill="#fff"/></svg>
          <span>5120 Ridgemont Pkwy.<br>Suite 400, Atlanta, GA 30327</span>
        </li>
        <li>
          <svg viewBox="0 0 16 16"><path d="M4 1l3 3-2 2c1 2 3 4 5 5l2-2 3 3-2 3C7 15 1 9 1 3z" fill="#fff"/></svg>
          <span>404.617.####<svg class="inline-icon" viewBox="0 0 16 16"><circle cx="8" cy="8" r="7" fill="#fff"/><path d="M4 6h8v2H4zM5 9h6v3H5z" fill="#26386a"/></svg>770.245.6274</span>
        </li>
        <li>
          <svg viewBox="0 0 16 16"><circle cx="8" cy="8" r="7.5" fill="#fff"/><path d="M4 5.5h8v5H4z" fill="none" stroke="#26386a"/><path d="M4 5.5l4 3 4-3" fill="none" stroke="#26386a"/></svg>
          <span>email@brantleyestates.com</span>
        </li>
        <li>
          <svg viewBox="0 0 16 16"><circle cx="8" cy="8" r="7" fill="none" stroke="#fff" stroke-width="1.3"/><ellipse cx="8" cy="8" rx="3" ry="7" fill="none" stroke="#fff"/><path d="M1 8h14M2.5 4.5h11M2.5 11.5h11" stroke="#fff"/></svg>
          <span>www.brantleyestates.com</span>
        </li>
      </ul>
    </div>
  </div>

  <div class="panel inside-right">
    <div class="pocket">
      <div class="card-slot">
        <div class="business-card">
          <div class="card-brand"><span class="dot"></span><span>BRANTLEY<br>ESTATES</span></div>
          <div class="card-details">
            <div class="name">Martin E. Caldwell</div>
            <div>Chairman &amp; CEO</div>
            <div>5120 Ridgemont Pkwy.</div>
            <div>Suite 400, Atlanta, GA 30327</div>
            <div>404.617.#### · 770.245.62##</div>
            <div>email@brantleyestates.com</div>
            <div>www.brantleyestates.com</div>
          </div>
        </div>
      </div>
      <div class="services">DEVELOPMENT LEASING | PROPERTY MANAGEMENT.</div>
    </div>
  </div>
</section>

</body>
</html>
```